Business card design needed

Card needs to say

Maren Fuldwick
Investor - Solutions - Development

My business is in property deals. I would like the words above to be on the card. I have attached a logo for you to copy/recreate.
On the back you could list the following:

Creative property solutions

Thankyou, Maren

Target Market(s)

people wanting to get into the property market, desperate sellers, Mums & Dads wanting to help their kids to purchase a property. People who want to create wealth. People who are stuck and need a solution.

Industry/Entity Type

Business

Contact Information for Business Card

T: 0431 205 774
F: (07) 3842 1597
E: maren47@vexlo.com.au

Requirements
Must have
• Simple and effective.
Look like I am here to help
Should not have
• Should not look like a realestate agent

```html
<!DOCTYPE html>
<html lang="en">
<head>
<meta charset="utf-8">
<title>Maren Fuldwick – Business Card</title>
<link rel="stylesheet" href="https://fonts.googleapis.com/css2?family=Arimo:wght@400;700&display=swap">
<style>
  :root {
    --backdrop: #3b3b3b;
    --card: #231f20;
    --green: #8dc63f;
    --grey: #a7a9ac;
  }
  html, body {
    margin: 0;
    padding: 0;
    width: 1200px;
    height: 900px;
    overflow: hidden;
    background: var(--backdrop);
    font-family: "Arimo", Arial, sans-serif;
  }
  .card {
    position: absolute;
    top: 300px;
    width: 525px;
    height: 296px;
    background: var(--card);
    overflow: hidden;
  }
  .card--front { left: 58px; }
  .card--back { left: 617px; }

  .brand-mark {
    position: absolute;
    width: 22px;
    height: 22px;
    background: var(--green);
  }
  .card--front .brand-mark { left: 252px; top: 116px; }
  .card--back .brand-mark { right: 38px; top: 128px; }

  .holder-name {
    position: absolute;
    margin: 0;
    font-weight: 700;
    color: var(--green);
    line-height: 1;
    white-space: nowrap;
  }
  .tagline {
    position: absolute;
    margin: 0;
    font-weight: 700;
    color: var(--grey);
    line-height: 1;
    white-space: nowrap;
  }

  .card--front .holder-name {
    left: 0; right: 0; top: 160px;
    text-align: center;
    font-size: 32px;
    letter-spacing: -0.3px;
  }
  .card--front .tagline {
    left: 0; right: 0; top: 191px;
    text-align: center;
    font-size: 11px;
  }

  .card--back .holder-name {
    right: 38px; top: 176px;
    font-size: 25px;
    letter-spacing: -0.2px;
  }
  .card--back .tagline {
    right: 38px; top: 200px;
    font-size: 11.5px;
  }
  .contact-list {
    position: absolute;
    right: 38px;
    top: 231px;
    margin: 0;
    padding: 0;
    list-style: none;
    text-align: right;
    font-size: 12px;
    font-weight: 700;
    color: var(--grey);
    line-height: 15px;
  }
  .contact-label { color: var(--green); }
</style>
</head>
<body>
  <section class="card card--front" aria-label="Card front">
    <span class="brand-mark" aria-hidden="true"></span>
    <h1 class="holder-name">Maren Fuldwick</h1>
    <p class="tagline">Investor - Solutions - Development</p>
  </section>

  <section class="card card--back" aria-label="Card back">
    <span class="brand-mark" aria-hidden="true"></span>
    <h2 class="holder-name">Maren Fuldwick</h2>
    <p class="tagline">Creative property solutions</p>
    <ul class="contact-list">
      <li><span class="contact-label">T:</span> 0431 205 774 <span class="contact-label">F:</span> (07) 3842 1597</li>
      <li><span class="contact-label">E:</span> maren47@vexlo.com.au</li>
    </ul>
  </section>
</body>
</html>
```